Web Design and logo

A new company based on creative professionals.. linking their artistic resources. Art, photography, music, and writing.

Target Market(s)

Artists buyers

Industry/Entity Type

It Company

Coding

Coded - Design and coding required

Number of Pages Required

3 page

Font styles to use
Decorative

Colors

Designer to choose colors to be used in the design.

Requirements
Nice to have
• Logo design based on Lively Maker Guild

```html
<!DOCTYPE html>
<html lang="en">
<head>
<meta charset="utf-8">
<title>Lively Maker Guild</title>
<link rel="stylesheet" href="https://fonts.googleapis.com/css2?family=Lato:wght@400;700;900&family=Oswald:wght@500;600&family=Open+Sans:ital,wght@0,400;0,700;1,400&display=swap">
<style>
:root{
  --blue:#1a6fb8;
  --blue-dark:#0f5e9e;
  --band:#2f7dc4;
  --ink:#333333;
  --heading:#2a2a2a;
  --muted:#777777;
  --line:#dcdcdc;
  --soft:#f4f4f4;
  --white:#ffffff;
  --star:#f2c40f;
}
*{box-sizing:border-box;margin:0;padding:0}
html,body{width:1200px;height:2497px;overflow:hidden}
body{position:relative;background:var(--white);font-family:"Lato",sans-serif;color:var(--ink)}
.abs{position:absolute}

/* header */
.site-header{position:absolute;left:0;top:0;width:1200px;height:77px;background:var(--white);border-top:3px solid var(--blue)}
.brand{position:absolute;left:131px;top:22px;font-size:25px;font-weight:700;color:#4a4a4a;letter-spacing:.2px}
.main-nav{position:absolute;top:30px;left:0;width:1200px;font-size:13px;color:#444}
.main-nav span{position:absolute}
.main-nav .active{color:var(--blue)}
.search-icon{position:absolute;left:1052px;top:27px}

/* hero */
.hero{position:absolute;left:0;top:77px;width:1200px;height:499px;
  background:linear-gradient(100deg,#6e7680 0%,#a9b0b7 35%,#cfd2d4 60%,#e7e3de 100%)}
.hero-title{position:absolute;left:131px;top:236px;font-family:"Oswald",sans-serif;font-weight:600;font-size:50px;color:var(--white);letter-spacing:.5px}
.hero-text{position:absolute;left:131px;top:300px;font-size:16px;font-weight:700;line-height:25px;color:var(--white)}
.hero-btn{position:absolute;left:131px;top:369px;width:137px;height:40px;border-radius:20px;background:var(--blue);color:var(--white);font-size:13px;font-weight:700;display:flex;align-items:center;justify-content:center;gap:5px}
.hero-dots{position:absolute;top:521px;left:984px;display:flex;gap:11px}
.hero-dots i{width:12px;height:12px;border-radius:50%;border:1.5px solid rgba(255,255,255,.9)}
.hero-dots i.on{background:var(--blue);border-color:var(--blue)}

/* services */
.services{position:absolute;left:0;top:576px;width:1200px;height:765px;background:var(--soft)}
.section-title{font-weight:900;font-size:30px;color:var(--heading);text-align:center}
.services .section-title{position:absolute;top:60px;width:1200px}
.services-intro{position:absolute;top:104px;width:1200px;text-align:center;font-size:12px;line-height:22px;color:#555}
.service-card{position:absolute;width:455px;height:231px;background:var(--white);border:1px solid var(--line)}
.service-photo{position:absolute;left:25px;top:13px;width:196px;height:196px;border-radius:50%;border:2px dotted #c8c8c8;display:flex;align-items:center;justify-content:center}
.service-photo div{width:178px;height:178px;border-radius:50%}
.service-name{position:absolute;left:240px;top:34px;font-size:17px;font-weight:700;color:var(--heading)}
.service-text{position:absolute;left:240px;top:64px;width:196px;font-size:12px;line-height:21px;color:var(--muted)}
.btn-small{position:absolute;left:240px;top:156px;width:105px;height:36px;border-radius:18px;background:var(--blue);color:var(--white);font-size:11px;font-weight:700;display:flex;align-items:center;justify-content:center}

/* recent work */
.work-frame{position:absolute;border:1px solid #d9d9d9;background:var(--white)}
.work-image{position:absolute;left:153px;top:1444px;width:355px;height:353px;background:radial-gradient(circle at 50% 50%,#e6e8ea 0%,#f6f6f6 60%,#fbfbfb 100%);border:1px solid #e2e2e2}
.work-title{position:absolute;left:624px;top:1440px;font-size:30px;font-weight:900;color:var(--heading)}
.work-intro{position:absolute;left:624px;top:1492px;width:450px;font-size:13px;font-weight:700;line-height:23px;color:#333}
.work-list{position:absolute;left:624px;top:1556px;width:450px;list-style:none}
.work-list li{position:relative;padding-left:32px;font-size:12px;line-height:22px;color:var(--muted);margin-bottom:21px}
.work-list svg{position:absolute;left:0;top:4px}

/* testimonials */
.testimonials{position:absolute;left:0;top:1899px;width:1200px;height:276px;
  background:linear-gradient(90deg,#2c79c0 0%,#3785c9 45%,#2a73b6 100%)}
.testimonial{position:absolute;top:61px;width:300px;color:var(--white)}
.avatar{position:absolute;left:0;top:0;width:66px;height:66px;border-radius:50%;border:3px solid var(--white);background:linear-gradient(160deg,#d9b89a,#8a6a55)}
.quote{position:absolute;left:87px;top:-1px;width:200px;font-family:"Open Sans",sans-serif;font-style:italic;font-size:12px;line-height:20px}
.quote b{font-family:Georgia,serif;font-size:18px;margin-right:6px;font-style:italic}
.person{position:absolute;left:87px;top:90px;font-family:"Open Sans",sans-serif;font-size:11px;font-weight:700}
.role{position:absolute;left:87px;top:110px;font-family:"Open Sans",sans-serif;font-style:italic;font-size:11px;opacity:.9}
.stars{position:absolute;left:87px;top:133px;display:flex;gap:3px}

/* footer */
.site-footer{position:absolute;left:0;top:2175px;width:1200px;height:271px;background:var(--soft)}
.foot-col{position:absolute;top:53px}
.foot-col h4{font-size:15px;font-weight:700;color:var(--heading);margin-bottom:14px}
.foot-col ul{list-style:none;font-size:12px;line-height:25px;color:#555}
.divider{position:absolute;top:50px;width:1px;height:162px;background:var(--line)}
.contact-line{position:relative;padding-left:25px;font-size:12px;color:#555;line-height:20px;margin-bottom:18px}
.contact-line svg{position:absolute;left:0;top:3px}
.news-text{font-size:12px;line-height:21px;color:#444;width:250px}
.field{position:absolute;height:39px;background:var(--white);border:1px solid #e0e0e0;font-size:11px;color:#444;padding-left:13px;display:flex;align-items:center}
.subscribe{position:absolute;height:39px;background:var(--blue);color:var(--white);font-size:12px;font-weight:700;display:flex;align-items:center;justify-content:center}
.copyright{position:absolute;left:0;top:2446px;width:1200px;height:51px;background:var(--white);text-align:center;font-size:11px;line-height:51px;color:#555;letter-spacing:.3px}
</style>
</head>
<body>

<header class="site-header">
  <div class="brand">Lively Maker Guild</div>
  <nav class="main-nav">
    <span class="active" style="left:585px">Home</span>
    <span style="left:648px">About Us</span>
    <span style="left:729px">What we do</span>
    <span style="left:823px">Testimonils</span>
    <span style="left:914px">Blog</span>
    <span style="left:971px">Contact Us</span>
  </nav>
  <svg class="search-icon" width="17" height="17" viewBox="0 0 17 17" fill="none" stroke="#999" stroke-width="1.6"><circle cx="7" cy="7" r="5.5"/><line x1="11" y1="11" x2="15.5" y2="15.5"/></svg>
</header>

<section class="hero" role="img" aria-label="Hero photo: hands drawing with a stylus on a graphics tablet beside a keyboard and colour swatches"></section>
<h1 class="hero-title">Creative Professionals</h1>
<p class="hero-text">Aliquip ex ea commodo consequat.aute irure reprehenderit<br>in voluptate velit esse cillum dolore fugiat...</p>
<div class="hero-btn">Learn More Info
  <svg width="12" height="12" viewBox="0 0 12 12" fill="none" stroke="#fff" stroke-width="1.3"><circle cx="6" cy="6" r="5"/><path d="M5 3.8 7.2 6 5 8.2"/></svg>
</div>
<div class="hero-dots"><i class="on"></i><i></i><i></i><i></i></div>

<section class="services">
  <h2 class="section-title">What We Do?</h2>
  <p class="services-intro">Aliquip ex ea commodo consequat. Duis aute irure dolor in reprehenderit in voluptate velit esse cillum dolore eu fugiat nulla pariatur<br>Excepteur sint occaecat cupidatat non proident, sunt in culpa qui officia</p>
</section>

<article class="service-card" style="left:131px;top:759px">
  <div class="service-photo"><div role="img" aria-label="Photo: hands painting at an art desk" style="background:linear-gradient(135deg,#f3ece4,#d9a7a0 60%,#c77b7a)"></div></div>
  <h3 class="service-name">Art</h3>
  <p class="service-text">Aliquip ex ea commodo consequat. Duis aute irure dolor in reprehenderit in voluptate velit esse cillum dolore eu fugiat nulla pariatur...</p>
  <div class="btn-small">Learn More Info</div>
</article>
<article class="service-card" style="left:614px;top:759px">
  <div class="service-photo"><div role="img" aria-label="Photo: photographer holding a camera" style="background:linear-gradient(135deg,#9aa692,#4f5d45 60%,#2f3a2b)"></div></div>
  <h3 class="service-name">Photography</h3>
  <p class="service-text">Aliquip ex ea commodo consequat. Duis aute irure dolor in reprehenderit in voluptate velit esse cillum dolore eu fugiat nulla pariatur...</p>
  <div class="btn-small">Learn More Info</div>
</article>
<article class="service-card" style="left:131px;top:1022px">
  <div class="service-photo"><div role="img" aria-label="Photo: hands playing an acoustic guitar" style="background:linear-gradient(135deg,#3a2b3e,#a4683a 55%,#1c1420)"></div></div>
  <h3 class="service-name">Music</h3>
  <p class="service-text">Aliquip ex ea commodo consequat. Duis aute irure dolor in reprehenderit in voluptate velit esse cillum dolore eu fugiat nulla pariatur...</p>
  <div class="btn-small">Learn More Info</div>
</article>
<article class="service-card" style="left:614px;top:1022px">
  <div class="service-photo"><div role="img" aria-label="Photo: fountain pen nib writing on paper" style="background:linear-gradient(135deg,#f2f2f2,#bdbdbd 60%,#7e7e7e)"></div></div>
  <h3 class="service-name">Writing</h3>
  <p class="service-text">Aliquip ex ea commodo consequat. Duis aute irure dolor in reprehenderit in voluptate velit esse cillum dolore eu fugiat nulla pariatur...</p>
  <div class="btn-small">Learn More Info</div>
</article>

<div class="work-frame" style="left:140px;top:1426px;width:382px;height:384px;transform:rotate(-4deg)"></div>
<div class="work-frame" style="left:140px;top:1426px;width:382px;height:384px;transform:rotate(4deg)"></div>
<div class="work-image" role="img" aria-label="Photo: crystal chandelier on a white background"></div>
<h2 class="work-title">Our Recent Work</h2>
<p class="work-intro">Excepteur sint occaecat cupidatat non proident, sunt in culpa qui officia aute irure dolor in reprehenderit...</p>
<ul class="work-list">
  <li><svg width="18" height="18" viewBox="0 0 18 18" fill="none" stroke="#1a6fb8" stroke-width="1.3"><circle cx="9" cy="9" r="8"/><path d="M7.5 5.5 11 9l-3.5 3.5"/></svg>Aliquip ex ea commodo consequat. Duis aute irure dolor in reprehenderit ined tate velit esse cillum dolore eu fugiat nulla pariatur...</li>
  <li><svg width="18" height="18" viewBox="0 0 18 18" fill="none" stroke="#1a6fb8" stroke-width="1.3"><circle cx="9" cy="9" r="8"/><path d="M7.5 5.5 11 9l-3.5 3.5"/></svg>Aliquip ex ea commodo consequat. Duis aute irure dolor in reprehenderit ined tate velit esse cillum dolore eu fugiat nulla pariatur...</li>
  <li><svg width="18" height="18" viewBox="0 0 18 18" fill="none" stroke="#1a6fb8" stroke-width="1.3"><circle cx="9" cy="9" r="8"/><path d="M7.5 5.5 11 9l-3.5 3.5"/></svg>Aliquip ex ea commodo consequat. Duis aute irure dolor in reprehenderit ined tate velit esse cillum dolore eu fugiat nulla pariatur...</li>
  <li><svg width="18" height="18" viewBox="0 0 18 18" fill="none" stroke="#1a6fb8" stroke-width="1.3"><circle cx="9" cy="9" r="8"/><path d="M7.5 5.5 11 9l-3.5 3.5"/></svg>Aliquip ex ea commodo consequat. Duis aute irure dolor in reprehenderit ined tate velit esse cillum dolore eu fugiat nulla pariatur...</li>
</ul>

<section class="testimonials" role="img" aria-label="Blue-tinted background photo of people working in an office">
  <div class="testimonial" style="left:131px">
    <div class="avatar" role="img" aria-label="Client portrait"></div>
    <p class="quote"><b>"</b>At vero eos et accusamus et iustodi dignissimos ducimus qui blanditiipraes ium voluptatum deleniti atq.</p>
    <div class="person">DANA WHITFIELD</div>
    <div class="role">Eiusmod tempor incididunt magna</div>
    <div class="stars">
      <svg width="17" height="16" viewBox="0 0 24 23"><path d="M12 1l3.2 7 7.6.7-5.7 5 1.7 7.5L12 17.3 5.2 21.2l1.7-7.5-5.7-5 7.6-.7z" fill="var(--star)"/></svg>
      <svg width="17" height="16" viewBox="0 0 24 23"><path d="M12 1l3.2 7 7.6.7-5.7 5 1.7 7.5L12 17.3 5.2 21.2l1.7-7.5-5.7-5 7.6-.7z" fill="var(--star)"/></svg>
      <svg width="17" height="16" viewBox="0 0 24 23"><path d="M12 1l3.2 7 7.6.7-5.7 5 1.7 7.5L12 17.3 5.2 21.2l1.7-7.5-5.7-5 7.6-.7z" fill="var(--star)"/></svg>
      <svg width="17" height="16" viewBox="0 0 24 23"><path d="M12 1l3.2 7 7.6.7-5.7 5 1.7 7.5L12 17.3 5.2 21.2l1.7-7.5-5.7-5 7.6-.7z" fill="var(--star)"/></svg>
      <svg width="17" height="16" viewBox="0 0 24 23"><path d="M12 1l3.2 7 7.6.7-5.7 5 1.7 7.5L12 17.3 5.2 21.2l1.7-7.5-5.7-5 7.6-.7z" fill="none" stroke="var(--star)" stroke-width="1.8"/></svg>
    </div>
  </div>
  <div class="testimonial" style="left:459px">
    <div class="avatar" role="img" aria-label="Client portrait"></div>
    <p class="quote"><b>"</b>At vero eos et accusamus et iustodi dignissimos ducimus qui blanditiipraes ium voluptatum deleniti atq.</p>
    <div class="person">DANA WHITFIELD</div>
    <div class="role">Eiusmod tempor incididunt magna</div>
    <div class="stars">
      <svg width="17" height="16" viewBox="0 0 24 23"><path d="M12 1l3.2 7 7.6.7-5.7 5 1.7 7.5L12 17.3 5.2 21.2l1.7-7.5-5.7-5 7.6-.7z" fill="var(--star)"/></svg>
      <svg width="17" height="16" viewBox="0 0 24 23"><path d="M12 1l3.2 7 7.6.7-5.7 5 1.7 7.5L12 17.3 5.2 21.2l1.7-7.5-5.7-5 7.6-.7z" fill="var(--star)"/></svg>
      <svg width="17" height="16" viewBox="0 0 24 23"><path d="M12 1l3.2 7 7.6.7-5.7 5 1.7 7.5L12 17.3 5.2 21.2l1.7-7.5-5.7-5 7.6-.7z" fill="var(--star)"/></svg>
      <svg width="17" height="16" viewBox="0 0 24 23"><path d="M12 1l3.2 7 7.6.7-5.7 5 1.7 7.5L12 17.3 5.2 21.2l1.7-7.5-5.7-5 7.6-.7z" fill="var(--star)"/></svg>
      <svg width="17" height="16" viewBox="0 0 24 23"><path d="M12 1l3.2 7 7.6.7-5.7 5 1.7 7.5L12 17.3 5.2 21.2l1.7-7.5-5.7-5 7.6-.7z" fill="none" stroke="var(--star)" stroke-width="1.8"/></svg>
    </div>
  </div>
  <div class="testimonial" style="left:785px">
    <div class="avatar" role="img" aria-label="Client portrait"></div>
    <p class="quote"><b>"</b>At vero eos et accusamus et iustodi dignissimos ducimus qui blanditiipraes ium voluptatum deleniti atq.</p>
    <div class="person">DANA WHITFIELD</div>
    <div class="role">Eiusmod tempor incididunt magna</div>
    <div class="stars">
      <svg width="17" height="16" viewBox="0 0 24 23"><path d="M12 1l3.2 7 7.6.7-5.7 5 1.7 7.5L12 17.3 5.2 21.2l1.7-7.5-5.7-5 7.6-.7z" fill="var(--star)"/></svg>
      <svg width="17" height="16" viewBox="0 0 24 23"><path d="M12 1l3.2 7 7.6.7-5.7 5 1.7 7.5L12 17.3 5.2 21.2l1.7-7.5-5.7-5 7.6-.7z" fill="var(--star)"/></svg>
      <svg width="17" height="16" viewBox="0 0 24 23"><path d="M12 1l3.2 7 7.6.7-5.7 5 1.7 7.5L12 17.3 5.2 21.2l1.7-7.5-5.7-5 7.6-.7z" fill="var(--star)"/></svg>
      <svg width="17" height="16" viewBox="0 0 24 23"><path d="M12 1l3.2 7 7.6.7-5.7 5 1.7 7.5L12 17.3 5.2 21.2l1.7-7.5-5.7-5 7.6-.7z" fill="var(--star)"/></svg>
      <svg width="17" height="16" viewBox="0 0 24 23"><path d="M12 1l3.2 7 7.6.7-5.7 5 1.7 7.5L12 17.3 5.2 21.2l1.7-7.5-5.7-5 7.6-.7z" fill="none" stroke="var(--star)" stroke-width="1.8"/></svg>
    </div>
  </div>
</section>

<footer class="site-footer">
  <div class="foot-col" style="left:131px">
    <h4>Quick Links</h4>
    <ul><li>Home</li><li>About Us</li><li>Our Services</li><li>Testimonials</li><li>Short Sale Info</li><li>Contact Us</li></ul>
  </div>
  <div class="divider" style="left:246px"></div>
  <div class="foot-col" style="left:285px">
    <h4>Information</h4>
    <ul><li>Terms &amp; Conditions</li><li>Privacy Policy</li><li>Disclaimer</li><li>Site Map</li><li>Faq</li></ul>
  </div>
  <div class="divider" style="left:438px"></div>
  <div class="foot-col" style="left:471px">
    <h4>Contact Us</h4>
    <div class="contact-line"><svg width="13" height="16" viewBox="0 0 13 16"><path d="M6.5 0A6 6 0 0 0 .5 6c0 4.5 6 10 6 10s6-5.5 6-10a6 6 0 0 0-6-6zm0 8.5A2.5 2.5 0 1 1 6.5 3.5a2.5 2.5 0 0 1 0 5z" fill="var(--blue)"/></svg>23#livelymakerguild<br>Street Name,City-545</div>
    <div class="contact-line"><svg width="14" height="14" viewBox="0 0 14 14"><path d="M3 0.5 5.2 3.5 4 5.4c.9 1.8 2.6 3.5 4.4 4.4l1.9-1.2 3 2.2-1.3 2.5C6 13 1 8 .6 1.8z" fill="var(--blue)"/></svg>Phone: 555-010-2309</div>
    <div class="contact-line"><svg width="14" height="11" viewBox="0 0 14 11"><rect x="0" y="0" width="14" height="11" rx="1" fill="var(--blue)"/><path d="M0.5 1 7 6 13.5 1" fill="none" stroke="#fff" stroke-width="1.2"/></svg>Email: info@livelymakerguild.com</div>
  </div>
  <div class="divider" style="left:789px"></div>
  <div class="foot-col" style="left:822px">
    <h4>Newsletter</h4>
    <p class="news-text">Get the latest updates on our courses and events: Notify Me</p>
  </div>
  <div class="field" style="left:822px;top:131px;width:245px">Enter Name</div>
  <div class="field" style="left:822px;top:178px;width:153px">Enter Email</div>
  <div class="subscribe" style="left:975px;top:178px;width:92px">Subscribe</div>
</footer>

<div class="copyright">©2017 &nbsp;LIVELYMAKERGUILD. ALL RIGHTS RESERVED.</div>

</body>
</html>
```